Korimet Business Cards

Korimet is a software startup and we are looking for business cards that help convey our employee personalities, as well as the professionalism of the company.
Our company font is Comfortaa - and the company logo is attached (we are okay having the text beside the logo if applicable) where we can find the company colour scheme. Cards can be horizontal or vertical format.
We are looking for a two sided business card - on the front we will see the personal details of the employee (name, position, email and phone number), and then on the back, we will see the business details (name and logo, address, phone number, website, email, company tagline: "Powering bold software change across the mobility industry")
We want the design to be clean and simple, but also fun, modern, and capturing of a young startup vibe.

```html
<!DOCTYPE html>
<html lang="en">
<head>
<meta charset="utf-8">
<title>Korimet Business Cards</title>
<link href="https://fonts.googleapis.com/css2?family=Montserrat:ital,wght@0,400;0,700;1,400&display=swap" rel="stylesheet">
<style>
  :root {
    --backdrop: #2b2b2d;
    --card: #1b1b1c;
    --ink: #ffffff;
    --brand-violet: #5a4bb0;
    --brand-magenta: #b94fa4;
    --brand-lilac: #8c5fc4;
    --rule: #e6e6e6;
  }
  * { box-sizing: border-box; margin: 0; padding: 0; }
  html, body { width: 1200px; height: 1200px; overflow: hidden; }
  body {
    background: var(--backdrop);
    font-family: "Montserrat", sans-serif;
    color: var(--ink);
    display: flex;
    align-items: center;
    justify-content: center;
    gap: 60px;
  }
  .card {
    width: 440px;
    height: 700px;
    background: var(--card);
    border-radius: 28px;
    position: relative;
    overflow: hidden;
    box-shadow: 0 18px 40px rgba(0,0,0,.45);
  }
  .brand-name {
    font-family: "Montserrat", sans-serif;
    font-weight: 700;
    color: var(--brand-violet);
    display: flex;
    align-items: center;
    justify-content: center;
    gap: 16px;
    position: absolute;
    left: 0; right: 0;
    white-space: nowrap;
  }
  .brand-dot {
    display: inline-block;
    border-radius: 50%;
    background: var(--brand-violet);
    flex: none;
  }
  .front .brand-name { top: 170px; font-size: 58px; }
  .front .brand-dot { width: 40px; height: 40px; }
  .name-band {
    position: absolute;
    top: 350px; left: 0; right: 0;
    height: 110px;
    background: linear-gradient(90deg, var(--brand-magenta), var(--brand-lilac));
    text-align: center;
    padding-top: 26px;
  }
  .person-name { font-weight: 700; font-size: 30px; letter-spacing: 2px; }
  .person-role { font-weight: 400; font-size: 18px; margin-top: 4px; }
  .icon-row {
    display: flex;
    align-items: center;
    justify-content: center;
    gap: 10px;
  }
  .icon-row .rule { width: 80px; height: 1px; background: var(--rule); }
  .icon-tile {
    width: 30px; height: 30px;
    border-radius: 6px;
    background: linear-gradient(135deg, var(--brand-magenta), var(--brand-lilac));
    display: flex; align-items: center; justify-content: center;
  }
  .icon-tile svg { width: 18px; height: 18px; }
  .contact {
    text-align: center;
    font-size: 19px;
    line-height: 1.4;
    margin-top: 14px;
  }
  .front .contact-block { position: absolute; top: 510px; left: 0; right: 0; }
  .tagline {
    position: absolute; top: 70px; left: 44px; right: 44px;
    text-align: center; font-style: italic; font-size: 19px; line-height: 1.4;
  }
  .back .brand-name { top: 240px; font-size: 54px; }
  .back .brand-dot { width: 36px; height: 36px; }
  .back .contact-block { position: absolute; top: 420px; left: 0; right: 0; }
  .address-rule { width: 220px; height: 1px; background: var(--rule); margin: 16px auto 14px; }
  .address { text-align: center; font-size: 19px; line-height: 1.4; }
</style>
</head>
<body>

<section class="card front">
  <div class="brand-name"><span class="brand-dot"></span>Korimet</div>
  <div class="name-band">
    <div class="person-name">LIAM FORSYTH</div>
    <div class="person-role">CEO/Founder</div>
  </div>
  <div class="contact-block">
    <div class="icon-row">
      <span class="rule"></span>
      <span class="icon-tile">
        <svg viewBox="0 0 24 24" fill="#fff"><path d="M6.6 10.8a15 15 0 0 0 6.6 6.6l2.2-2.2a1 1 0 0 1 1-.25 11.4 11.4 0 0 0 3.6.57 1 1 0 0 1 1 1V20a1 1 0 0 1-1 1A17 17 0 0 1 3 4a1 1 0 0 1 1-1h3.5a1 1 0 0 1 1 1c0 1.25.2 2.45.57 3.57a1 1 0 0 1-.25 1z"/></svg>
      </span>
      <span class="icon-tile">
        <svg viewBox="0 0 24 24" fill="#fff"><path d="M3 6h18v12H3z"/><path d="M3 6l9 7 9-7" fill="none" stroke="#9a58b8" stroke-width="1.6"/></svg>
      </span>
      <span class="rule"></span>
    </div>
    <div class="contact">
      +123.555.0142<br>
      liam@korimet.com.au
    </div>
  </div>
</section>

<section class="card back">
  <p class="tagline">“Powering bold software change<br>across the mobility industry”</p>
  <div class="brand-name"><span class="brand-dot"></span>Korimet</div>
  <div class="contact-block">
    <div class="icon-row">
      <span class="rule"></span>
      <span class="icon-tile">
        <svg viewBox="0 0 24 24" fill="#fff"><path d="M6.6 10.8a15 15 0 0 0 6.6 6.6l2.2-2.2a1 1 0 0 1 1-.25 11.4 11.4 0 0 0 3.6.57 1 1 0 0 1 1 1V20a1 1 0 0 1-1 1A17 17 0 0 1 3 4a1 1 0 0 1 1-1h3.5a1 1 0 0 1 1 1c0 1.25.2 2.45.57 3.57a1 1 0 0 1-.25 1z"/></svg>
      </span>
      <span class="icon-tile">
        <svg viewBox="0 0 24 24" fill="#fff"><path d="M3 6h18v12H3z"/><path d="M3 6l9 7 9-7" fill="none" stroke="#9a58b8" stroke-width="1.6"/></svg>
      </span>
      <span class="icon-tile">
        <svg viewBox="0 0 24 24" fill="none" stroke="#fff" stroke-width="1.8"><circle cx="12" cy="12" r="9"/><path d="M3 12h18M12 3c3 3.2 3 14.8 0 18M12 3c-3 3.2-3 14.8 0 18"/></svg>
      </span>
      <span class="rule"></span>
    </div>
    <div class="contact">
      +987.555.0198<br>
      service@korimet.com.au<br>
      www.korimet.com.au
    </div>
    <div class="address-rule"></div>
    <div class="address">
      Elmwood, Harrow Street<br>
      Westfield Park, 2041
    </div>
  </div>
</section>

</body>
</html>
```